依頼詳細
概要、特徴にも書いたように、今回、分離発注に向けた営業用のチラシを作成して頂きたいです。

・すでに既存で新規顧客獲得用のパンフレット(高難度松浦工業)とチラシ(HARUKAZE)があり、今回は、それらに追加で挟む “分離発注を目的としたチラシ” の依頼となります。

※既存(高難度パンフレット)(添付資料1、2)
+
既存(HARUKAZE)(添付資料3)
+
“分離発注を目的としたチラシ”

既存の3つのチラシ(※添付資料1.2.3)と一緒に挟んで、配布したいので

流れを理解して作成していただけたら幸いです。

・流れ、
株式会社松浦工業は、高難度の足場を専門で営業しています。

また、その職人で構成されている、HARUKAZEというワンランク上の足場サービスも運営しています。(住人さんや近隣様、などへの配慮、最高のサービスを提供するブランド)
(HARUKAZEにもホームページがございます。)

安全には、費用がかかります。
人の命は尊いです。
工事は足場から始まり、足場で終わります。
そして、業者みんなが使う足場です。

弊社の売りを武器として運営し維持して行くためには、無駄な予算を削り、その予算を安心できる工事に生かす。

そして見た目も美しい職人で揃えている私たちと手を組みませんか。

。。。といった流れでイメージして作成して頂きたいです。

※弊社の売りに関しましては、添付した資料やホームページを確認して頂き、理解して頂きたいです。

・目的は、新規顧客の獲得ですが、分離発注の提案を載せたいです。

・新規顧客(ターゲット)→ビル建物のオーナー、元請業社、ゼネコンなど

・メリットとデメリットをまとめたマインドマップも添付しますので、必要であれば使ってください。
・他にも、ホームページもありますので、見ていただけたら、と思います。
・弊社は改修工事用の足場をメインで運営しております。
(居住者様や、近隣様、歩行者様からの安心や業者間、現場管理監督様とのコミュニケーションもとても大切にしております。)
・メリットのマインドマップの他にも、弊社を使うことでのメリットは、たくさんあります。
・どの立場から見ても美しい足場屋を目指しております。

記載項目
分離発注しませんか。

株式会社松浦工業
042−718−2964
https://matsuurakogyo-ashiba.example
↑↑
株式会社松浦工業(高難度専門の足場サービス)

https://harukaze-ashiba.example
↑↑
ワンランク上の足場サービス
HARUKAZE ホームページ

サイズ
A4
ページ数
両面
希望イメージ
シンプル 複雑
単色 カラフル
暗い 明るい
日常 高級
遊び心 厳粛
未来的 伝統的
女性的 男性的
希望する色
黄・オレンジ系、緑系、青系、既存チラシ(添付資料1.2.3)とのバランスで決めて頂きたい
納品ファイル
• 高解像度JPG (.jpg)
• イラストレーター形式 (.ai)
補足説明
↑↑
株式会社松浦工業(高難度専門の足場サービス)

↑↑
ワンランク上の足場サービス
HARUKAZE ホームページ

どちらも並行して運営しております!

ーーーーーーーーーーーーーーーーーーーーーーーーー

※多少の文字の変更などがしやすいように、アウトライン化されていないデータでも納品して頂きたいです。
みなさま、すばらしい作品をありがとうございます!

みなさまの作品を見て間違えに気づくことが出来ました。

一部、変更させてください!

3点あるのですが、

①1つ目は、このチラシを誰に当てた手紙にするのか、ですが、ターゲットは、
・ビルやマンション、学校など建物のオーナー様
・ビルやマンションの管理をしている管理会社様や、
・不動産会社様
・店舗、等の工事担当者様
に当てた手紙で作成して頂きたいです。

※よく考えたら工事会社が直接足場屋に依頼するのは、当前のことだと思いましたので、工事業者に当てるのはおかしい話だと気付いたので宜しくお願いいたします。

②見積もり依頼までの流れを盛り込んで頂きたいです。
流れ
平日の9:00〜17:00に
042−718−2964

に電話をして頂き、弊社の電話に出た物に、見積もりして欲しい物件のご住所をお聞かせください。

or

当社ホームページ問い合わせフォームのQRコード?
かURL??

で見積もり依頼のメッセージを頂けたら、

1週間以内にTerravue Mapsを元に概算でお見積もりして郵送させて頂きます。

※建物の改修工事が決まりましたら、弊社と工事業者様とで直接お打ち合わせして、施工します!
※安心、安全へのクオリティは、高品質をお約束しますので、安心してください。
※足場工事は、命の危険を伴う工事です。

。。。のような感じをうまく刺さる形で表現して頂きたいです。

③ターゲットに分離発注という意味を理解してもらえるのかも不安になってきたのですが、どうでしょうか。

このチラシに足場だけを分離発注しませんか?なのか、
直接発注しませんか、なのか、何か良い表現があればそれも考えていただけると幸いです。

分離発注でわかるから大丈夫だよ、であれば分離発注も構いません。
ただ僕が不安になっただけなので、
そこも何か良い案があればなーと思ったので、宜しくお願いいたします。

コロナで、大ダメージを受けてしまったので、これで、復活したいと考えております!

みなさま、どうか宜しくお願いいたします!

弊社の既存のパンフレットと一緒に配ることを踏まえてこの作品が一番良いのではないかと感じました。

この度は、本当にありがとうございました。
僕たちは、職人さん達の生活がもっと潤っていけるように、したいと考えております。
職人さん達の世界では土曜も仕事をすることが当たり前となっております。
しかし僕たちは価値の高い仕事を社会に広めていき、みんなが、より良い工事をしながら、生活も潤っていけるように考えております。
皆さんが作ってくれた作品から、僕たちは大きな気づきをゲットしました!
とても感謝しています。
本当に本当にありがとうございました。

```html
<!DOCTYPE html>
<html lang="ja">
<head>
<meta charset="utf-8">
<title>分離発注のご提案 | 株式会社松浦工業</title>
<link href="https://fonts.googleapis.com/css2?family=Noto+Sans+JP:wght@400;500;700;900&display=swap" rel="stylesheet">
<style>
:root{
  --yellow:#ffd400;
  --ink:#1a1a1a;
  --blue:#1f63b4;
  --paper:#ffffff;
  --grey:#eceef1;
  --muted:#555;
}
*{box-sizing:border-box;margin:0;padding:0}
html,body{width:846px;height:1200px;overflow:hidden;background:var(--paper)}
body{font-family:"Noto Sans JP",sans-serif;color:var(--ink);position:relative}

.hero{position:absolute;left:0;top:0;width:846px;height:580px}
.hero-photo{position:absolute;left:300px;top:40px;width:546px;height:540px;
  background:linear-gradient(120deg,#f4e2c4 0%,#e0a25a 25%,#8a5a33 50%,#3a3536 75%,#18181a 100%)}
.hero-fade{position:absolute;left:300px;top:40px;width:546px;height:540px;
  background:linear-gradient(90deg,#fff 0%,rgba(255,255,255,.6) 30%,rgba(255,255,255,0) 60%),
             linear-gradient(0deg,#fff 0%,rgba(255,255,255,0) 25%)}
.tagline{position:absolute;left:32px;top:14px;font-size:22px;font-weight:900;letter-spacing:1px}
.tagline .mark{background:linear-gradient(transparent 55%,var(--yellow) 55%)}
.title{position:absolute;left:32px;top:100px}
.title span{display:inline-block;background:var(--yellow);font-weight:900;line-height:1;padding:12px 16px}
.title .main{font-size:82px;letter-spacing:6px}
.title .sub{font-size:72px;letter-spacing:6px;margin-top:18px}
.lead{position:absolute;left:0;top:338px;width:640px;padding:10px 0 10px 32px;font-size:13px;line-height:1.95;font-weight:500;text-align:center;
  background:linear-gradient(90deg,rgba(255,255,255,.95) 75%,rgba(255,255,255,0) 100%)}

.fee{position:absolute;left:0;top:585px;width:846px;height:235px}
.fee-head{position:absolute;left:32px;top:0;width:782px;border:1px solid #bcc6d3;border-left:8px solid var(--blue);padding:7px 14px;font-size:17px;font-weight:700}
.fee-head b{color:var(--blue);font-weight:900}
.chart{position:absolute;left:32px;top:55px;width:470px;height:170px}
.chart-title{position:absolute;left:110px;top:0;width:300px;text-align:center;font-size:10px;color:var(--muted)}
.axis{position:absolute;left:110px;top:18px;width:1px;height:148px;background:#999}
.row{position:absolute;left:0;width:470px;height:56px}
.row .label{position:absolute;left:0;top:0;width:105px;height:56px;display:flex;align-items:center;font-size:10px;line-height:1.4;color:var(--muted)}
.row .bar{position:absolute;left:110px;top:0;width:290px;height:56px;background:linear-gradient(90deg,#dbe7f5,var(--blue))}
.row .tip{position:absolute;left:400px;top:0;width:66px;height:56px;background:var(--yellow);display:flex;flex-direction:column;align-items:center;justify-content:center;font-size:12px;font-weight:900;line-height:1.2;text-align:center}
.row .tip small{font-size:8px;font-weight:500}
.row-a{top:24px}
.row-b{top:104px}
.fee-msg{position:absolute;left:540px;top:92px;border-left:6px solid var(--blue);padding-left:14px;font-size:22px;line-height:1.5;font-weight:900;color:var(--blue)}

.effort{position:absolute;left:0;top:830px;width:846px;height:370px;background:var(--grey)}
.effort-kicker{position:absolute;left:32px;top:18px;font-size:17px;font-weight:900}
.effort-title{position:absolute;left:32px;top:40px;font-size:30px;font-weight:900;letter-spacing:1px;line-height:1.3}
.effort-title::after{content:"";display:block;width:500px;height:3px;background:var(--yellow);margin-top:4px}
.effort-text{position:absolute;left:32px;top:100px;width:520px;font-size:10.5px;line-height:1.9}
.brand-photo{position:absolute;left:578px;top:18px;width:238px;height:150px;background:linear-gradient(160deg,#5b6470,#2c3340 60%,#1c2129)}
.brand-caption{position:absolute;left:578px;top:172px;width:238px;text-align:center;font-size:9px;color:var(--muted)}
.gallery{position:absolute;left:32px;top:296px;width:784px;height:74px;display:grid;grid-template-columns:repeat(5,1fr);gap:6px}
.gallery div{background:linear-gradient(150deg,#9aa4af,#4d5663)}
.gallery div:nth-child(2){background:linear-gradient(150deg,#d8d2c6,#7a6f60)}
.gallery div:nth-child(3){background:linear-gradient(150deg,#c7ccd3,#6a7480)}
.gallery div:nth-child(4){background:linear-gradient(150deg,#3f4a5a,#1f2630)}
.gallery div:nth-child(5){background:linear-gradient(150deg,#a9b3bd,#39414c)}
</style>
</head>
<body>

<section class="hero">
  <div class="hero-photo" role="img" aria-label="安全帯を装着して足場の上で作業する職人の写真"></div>
  <div class="hero-fade"></div>
  <p class="tagline"><span class="mark">安心・安全・高品質</span> な工事のために。</p>
  <h1 class="title"><span class="main">分離発注</span><br><span class="sub">のご提案</span></h1>
  <p class="lead">“高難度の足場” 専門の足場屋「株式会社松浦工業」は、<br>高品質な工事と安全・安心への取り組みに力を入れています。<br>この強みを維持して、工事に関わる全ての方の利益を追求するため、<br>足場の分離発注をご提案いたします。</p>
</section>

<section class="fee">
  <h2 class="fee-head"><b>中間手数料</b>を、安心・安全・高品質な工事のための費用に回しませんか？</h2>
  <div class="chart">
    <p class="chart-title">足場工事の金額比較</p>
    <div class="axis"></div>
    <div class="row row-a">
      <p class="label">中間業者を<br>経由した場合</p>
      <div class="bar"></div>
      <div class="tip">中間<br>手数料<small>（約1〜2割）</small></div>
    </div>
    <div class="row row-b">
      <p class="label">中間業者を<br>省いた場合</p>
      <div class="bar"></div>
      <div class="tip">安心・<br>安全<small>への費用</small></div>
    </div>
  </div>
  <p class="fee-msg">足場の分離発注で、<br>安心・安全への予算<br>が生まれます</p>
</section>

<section class="effort">
  <p class="effort-kicker">松浦工業の</p>
  <h2 class="effort-title">安心・安全への取り組みとは？</h2>
  <p class="effort-text">私たちは安心・安全への基本を大切に取り組んでいます。足場点検の徹底や安全講習の受講など、職人一人ひとりが高い意識を持って現場に立っています。また、居住者様や近隣の皆様、歩行者の方への配慮を第一に考え、丁寧な挨拶と整理整頓を欠かしません。業者間や現場管理者様との連携も大切にし、どの立場から見ても美しい足場を目指しています。ワンランク上の足場サービス「HARUKAZE」も運営しています。</p>
  <div class="brand-photo" role="img" aria-label="揃いの作業着を着た職人たちの集合写真"></div>
  <p class="brand-caption">ワンランク上の足場サービス「HARUKAZE」</p>
  <div class="gallery">
    <div role="img" aria-label="安全講習を受ける職人の写真"></div>
    <div role="img" aria-label="組み上がった足場の写真"></div>
    <div role="img" aria-label="朝礼をする職人たちの写真"></div>
    <div role="img" aria-label="整列する職人たちの写真"></div>
    <div role="img" aria-label="足場を点検する職人の写真"></div>
  </div>
</section>

</body>
</html>
```